VORTEK Studio Shape your ideas

VORTEK Studio is a soci% 26 # 233; t% 26 # 233; of mobile application design and multiexperience destiny% 26 # 233; % 26 # 224; The% 26 # 39; industry and particularly the watch industry% 26 # 232; re. By multiexperience, I mean applications usable on watches,% 26 # 233; holographic screens,% 26 # 233; touch screens g% 26 # 233; ant, r% 26 # 233; alit% 26 # 233; virtual,% 26 # 224; distance with a gripsense and% 26 # 233; obviously on mobile on tablet and smartphone. Applications will call% 26 # 224; 3d, artificial intelligence, big data. The company logo% 26 # 233; t% 26 # 233; is attached% 26 # 233; below.

Target Market(s)

Swiss precision industry Watchmaking industry% 26 # 232; re

Coding

Coded - Design and coding required

Font styles to use
Sans Serif

Colors

Designer to choose colors to be used in the design.

Requirements
Must have
• A Contact form A gallery of Vid% 26 # 233; o / Photo (portfolio) 3D images of% 26 # 39; illustration orient% 26 # 233; es industry but% 26 # 233; also luxury (take free images A partner page
Nice to have
• A blog
Should not have
• The designs are too loaded, the page should load quickly.

```html
<!DOCTYPE html>
<html lang="en">
<head>
<meta charset="utf-8">
<title>VORTEK Studio</title>
<link href="https://fonts.googleapis.com/css2?family=Josefin+Sans:wght@300;400;600;700&family=Montserrat:wght@400;500;600;700&display=swap" rel="stylesheet">
<style>
:root{
  --blue:#0a6fc2;
  --blue-dark:#0558a3;
  --accent:#4a9fd8;
  --ink:#111;
  --text:#333;
  --white:#fff;
  --grey:#ececec;
  --black:#000;
}
*{margin:0;padding:0;box-sizing:border-box}
html,body{width:1200px;height:5383px;overflow:hidden}
body{position:relative;background:var(--white);font-family:"Montserrat",sans-serif;color:var(--text)}
.abs{position:absolute}
.btn{position:absolute;background:var(--blue);color:var(--white);font:700 14px "Montserrat",sans-serif;letter-spacing:.5px;display:flex;align-items:center;justify-content:center;text-transform:uppercase}
/* header */
.site-header{position:absolute;left:0;top:0;width:1200px;height:86px;background:var(--white)}
.brand{position:absolute;left:157px;top:20px;display:flex;align-items:center;gap:10px;font:700 26px "Josefin Sans",sans-serif;color:var(--blue-dark)}
.brand-mark{width:18px;height:18px;background:var(--blue)}
.nav{position:absolute;top:34px;font:500 13px "Montserrat",sans-serif;color:#222;text-transform:uppercase}
/* hero */
.hero{position:absolute;left:0;top:86px;width:1200px;height:562px;background:linear-gradient(120deg,#3a4450 0%,#1d2836 45%,#2a3442 70%,#131a24 100%)}
.hero-title{position:absolute;left:157px;top:130px;font:700 68px "Josefin Sans",sans-serif;color:var(--white);line-height:1}
.hero-sub{position:absolute;left:157px;top:196px;font:400 38px "Josefin Sans",sans-serif;color:var(--white);line-height:44px}
.hero-wave{position:absolute;left:0;bottom:0}
/* deco squares */
.deco{position:absolute}
.deco::before{content:"";position:absolute;left:-22%;top:22%;width:100%;height:100%;background:var(--grey)}
.deco::after{content:"";position:absolute;inset:0;background:var(--white);box-shadow:0 2px 10px rgba(0,0,0,.22)}
/* sections */
.section-title{position:absolute;left:0;width:1200px;text-align:center;font:300 54px "Josefin Sans",sans-serif;color:var(--ink)}
.lead{position:absolute;left:180px;width:840px;text-align:center;font:400 18px/27px "Montserrat",sans-serif;color:#333}
.feature-num{position:absolute;font:700 30px "Josefin Sans",sans-serif;color:var(--accent)}
.feature-title{position:absolute;width:440px;font:700 33px/42px "Josefin Sans",sans-serif;color:var(--ink);text-transform:uppercase}
.feature-text{position:absolute;width:430px;font:400 13px/24px "Montserrat",sans-serif;color:#333}
.blob{position:absolute;overflow:hidden}
.blob-a{border-radius:58% 42% 50% 50% / 45% 50% 50% 55%}
.blob-b{border-radius:45% 55% 40% 60% / 55% 45% 55% 45%}
.ring{position:absolute;border:2px dashed var(--accent);border-radius:50%}
/* services */
.services-band{position:absolute;left:0;top:3831px}
.services-title{position:absolute;left:0;top:3910px;width:1200px;text-align:center;font:300 58px "Josefin Sans",sans-serif;color:var(--white);letter-spacing:1px}
.service-img{position:absolute;top:4008px;width:285px;height:304px}
.service-cap{position:absolute;top:4330px;font:400 28px "Josefin Sans",sans-serif;color:var(--ink)}
/* contact */
.email-field{position:absolute;left:349px;top:4655px;width:504px;height:44px;background:var(--white);box-shadow:0 3px 12px rgba(0,0,0,.2);font:500 13px "Montserrat",sans-serif;color:#222;display:flex;align-items:center;justify-content:center}
/* footer */
.site-footer{position:absolute;left:0;top:4860px}
.foot-col{position:absolute;top:5062px;color:var(--white)}
.foot-col h4{font:400 19px "Josefin Sans",sans-serif;margin-bottom:8px}
.foot-col li{list-style:none;font:500 12px/27px "Montserrat",sans-serif}
.copyright{position:absolute;left:157px;top:5284px;font:500 14px "Montserrat",sans-serif;color:var(--white)}
.social{position:absolute;top:5278px;width:32px;height:32px;border-radius:50%;background:var(--white)}
</style>
</head>
<body>

<header class="site-header">
  <div class="brand"><span class="brand-mark"></span>VORTEK Studio</div>
  <span class="nav" style="left:483px">The Lab</span>
  <span class="nav" style="left:593px">Why Vortek</span>
  <span class="nav" style="left:736px">Contact Us</span>
  <span class="btn" style="left:892px;top:21px;width:150px;height:46px">Get in touch</span>
</header>

<section class="hero" role="img" aria-label="Hands holding a smartphone showing a data dashboard">
  <h1 class="hero-title">VORTEK STUDIO</h1>
  <p class="hero-sub">Mobile and Multiexperience<br>Application Design Company</p>
  <span class="btn" style="left:157px;top:299px;width:134px;height:46px">About us</span>
  <svg class="hero-wave" width="1200" height="200" viewBox="0 0 1200 200"><path d="M0,200 L0,150 C40,90 120,60 220,70 C420,90 560,170 800,175 C960,178 1100,150 1200,110 L1200,200 Z" fill="#fff"/></svg>
</section>

<div class="deco" style="left:124px;top:620px;width:128px;height:128px"></div>
<div class="deco" style="left:276px;top:562px;width:60px;height:60px"></div>
<div class="deco" style="left:1036px;top:720px;width:58px;height:58px"></div>
<div class="deco" style="left:1100px;top:810px;width:58px;height:58px"></div>
<div class="deco" style="left:48px;top:886px;width:126px;height:126px"></div>
<div class="deco" style="left:1072px;top:922px;width:128px;height:132px"></div>

<h2 class="section-title" style="top:758px">THE LAB</h2>
<p class="lead" style="top:823px">It is a long established fact that a reader will be distracted by the readable content of a page when looking at its layout. The point of using Lorem Ipsum is that it has a more-or-less normal distribution of letters.</p>
<span class="btn" style="left:533px;top:928px;width:132px;height:46px">About us</span>

<h2 class="section-title" style="top:1115px">WHY VORTEK</h2>

<div class="ring" style="left:-52px;top:1171px;width:522px;height:522px"></div>
<div class="blob blob-a" style="left:157px;top:1269px;width:407px;height:393px;background:linear-gradient(135deg,#e4e6ea,#5a6e8a 55%,#c9b3a2)" role="img" aria-label="Smartwatch and smartphone showing fitness charts"></div>
<div class="deco" style="left:980px;top:1246px;width:60px;height:60px"></div>
<span class="feature-num" style="left:606px;top:1318px">1.</span>
<h3 class="feature-title" style="left:606px;top:1374px">Usable on watches</h3>
<p class="feature-text" style="left:606px;top:1422px">It is a long established fact that a reader will be distracted by the readable content of a page when looking at its layout. The point of using Lorem Ipsum is that it has a more-or-less normal distribution of letters.</p>

<div class="deco" style="left:472px;top:1720px;width:60px;height:60px"></div>
<span class="feature-num" style="left:157px;top:1754px">2.</span>
<h3 class="feature-title" style="left:157px;top:1810px">Holographic screens</h3>
<p class="feature-text" style="left:157px;top:1858px">It is a long established fact that a reader will be distracted by the readable content of a page when looking at its layout. The point of using Lorem Ipsum is that it has a more-or-less normal distribution of letters.</p>
<div class="blob blob-b" style="left:635px;top:1632px;width:406px;height:393px;background:radial-gradient(circle at 50% 50%,#6fa9c8,#2b3b46 55%,#121418)" role="img" aria-label="Holographic display projected around a wrist"></div>

<div class="blob blob-b" style="left:157px;top:2050px;width:407px;height:391px;background:linear-gradient(135deg,#8b5a48,#c98c73 45%,#3a2a28)" role="img" aria-label="Finger tapping a smartwatch on a wrist"></div>
<div class="deco" style="left:976px;top:2074px;width:62px;height:62px"></div>
<span class="feature-num" style="left:617px;top:2135px">3.</span>
<h3 class="feature-title" style="left:617px;top:2190px">Giant touch screens</h3>
<p class="feature-text" style="left:617px;top:2238px">It is a long established fact that a reader will be distracted by the readable content of a page when looking at its layout. The point of using Lorem Ipsum is that it has a more-or-less normal distribution of letters.</p>

<div class="deco" style="left:472px;top:2488px;width:62px;height:62px"></div>
<span class="feature-num" style="left:157px;top:2534px">4.</span>
<h3 class="feature-title" style="left:157px;top:2588px">Virtual reality</h3>
<p class="feature-text" style="left:157px;top:2636px">It is a long established fact that a reader will be distracted by the readable content of a page when looking at its layout. The point of using Lorem Ipsum is that it has a more-or-less normal distribution of letters.</p>
<div class="blob blob-a" style="left:635px;top:2447px;width:406px;height:391px;background:radial-gradient(circle at 55% 50%,#2f6ea8,#123052 45%,#04070c 75%)" role="img" aria-label="Person wearing a virtual reality headset reaching forward"></div>

<div class="blob blob-a" style="left:157px;top:2853px;width:407px;height:393px;background:linear-gradient(135deg,#f2f2f2,#d9d4c8 50%,#e3b02a)" role="img" aria-label="Person in a yellow jacket wearing a headset and holding a laptop"></div>
<div class="deco" style="left:978px;top:2866px;width:62px;height:62px"></div>
<span class="feature-num" style="left:617px;top:2916px">5.</span>
<h3 class="feature-title" style="left:617px;top:2970px">Remotely with a gripsense</h3>
<p class="feature-text" style="left:617px;top:3052px">It is a long established fact that a reader will be distracted by the readable content of a page when looking at its layout. The point of using Lorem Ipsum is that it has a more-or-less normal distribution of letters.</p>

<div class="ring" style="left:732px;top:3261px;width:500px;height:500px"></div>
<div class="deco" style="left:472px;top:3314px;width:62px;height:62px"></div>
<span class="feature-num" style="left:157px;top:3372px">6.</span>
<h3 class="feature-title" style="left:157px;top:3428px">Mobile on tablet and smartphone</h3>
<p class="feature-text" style="left:157px;top:3508px">It is a long established fact that a reader will be distracted by the readable content of a page when looking at its layout. The point of using Lorem Ipsum is that it has a more-or-less normal distribution of letters.</p>
<div class="blob blob-b" style="left:635px;top:3294px;width:406px;height:447px;background:linear-gradient(160deg,#1a1f2a,#2a3140 50%,#6b4a30)" role="img" aria-label="Tablet and smartwatch showing fitness statistics"></div>

<svg class="services-band" width="1200" height="560" viewBox="0 0 1200 560"><path d="M0,0 H1200 V250 C1000,280 800,250 600,255 C350,262 150,280 0,360 Z" fill="#0a6fc2"/></svg>
<h2 class="services-title">OTHER SERVICES</h2>
<div class="service-img" style="left:157px;background:linear-gradient(135deg,#2a3a55,#0b0f16 60%,#b5651d)" role="img" aria-label="Processor chip on a circuit board"></div>
<div class="service-img" style="left:460px;background:linear-gradient(90deg,#0b1a2e,#1e8a8a 50%,#0b1a2e)" role="img" aria-label="Glowing data server corridor"></div>
<div class="service-img" style="left:757px;background:radial-gradient(circle,#9fb4c8,#1f5a9a 45%,#0c2a55)" role="img" aria-label="Smartwatch over a blue digital background"></div>
<span class="service-cap" style="left:157px">Artificial intelligence</span>
<span class="service-cap" style="left:455px">Big Data</span>
<span class="service-cap" style="left:757px">3d</span>

<div class="deco" style="left:212px;top:4428px;width:60px;height:60px"></div>
<div class="deco" style="left:58px;top:4484px;width:126px;height:120px"></div>
<div class="deco" style="left:1035px;top:4695px;width:58px;height:58px"></div>
<div class="deco" style="left:1008px;top:4790px;width:130px;height:128px"></div>

<h2 class="section-title" style="top:4510px">GET IN TOUCH</h2>
<p class="lead" style="top:4580px;font-size:14px;line-height:23px">It is a long established fact that a reader will be distracted by the readable content of a page when looking at its layout</p>
<div class="email-field">Enter Your Mail ID</div>
<span class="btn" style="left:537px;top:4717px;width:134px;height:44px">Submit now</span>

<svg class="site-footer" width="1200" height="523" viewBox="0 0 1200 523"><path d="M0,30 C300,-10 700,70 1000,40 C1100,30 1160,20 1200,15 V523 H0 Z" fill="#000"/></svg>
<div class="foot-col" style="left:157px"><h4>The Platform</h4><ul><li>Features</li><li>Lorem ipsum</li><li>long established fact</li><li>Lorem ipsum</li><li>long established fact</li></ul></div>
<div class="foot-col" style="left:341px"><h4>Our Company</h4><ul><li>Lorem ipsum</li><li>Lorem ipsum</li><li>long established fact</li><li>Lorem ipsum</li><li>long established fact</li></ul></div>
<div class="foot-col" style="left:525px"><h4>Why Us?</h4><ul><li>Lorem ipsum</li><li>Lorem ipsum</li><li>long established fact</li><li>Lorem ipsum</li><li>long established fact</li></ul></div>
<div class="foot-col" style="left:713px"><h4>Resources</h4><ul><li>Lorem ipsum</li><li>Lorem ipsum</li><li>long established fact</li><li>Lorem ipsum</li><li>long established fact</li></ul></div>
<div class="foot-col" style="left:915px;top:5066px"><h4>Partnership</h4><ul><li>Lorem ipsum</li><li>Lorem ipsum</li><li>long established fact</li><li>Lorem ipsum</li><li>long established fact</li></ul></div>
<p class="copyright">Copyright©2020 VORTEK. All Rights Reserved.</p>
<span class="social" style="left:891px"></span>
<span class="social" style="left:931px"></span>
<span class="social" style="left:970px"></span>
<span class="social" style="left:1009px"></span>

</body>
</html>
```